Guaranteed Job - Sleek Sexy Business Card UV Spot

Im looking for a sleek and sexy business card, that resembles elite or VIP status status.
our business is corinvale.example
you can view our products on there, but our main audience for handing out our cards will be for people in the hospitality industry, so it will need to impress high management and CEO of hotels and restaurants, bars, clubs etc...
the card features will have UV spot on both sides, 400gsm stock. standard size.
Artwork should be 86 x 54mm + 2mm bleed = 90 x 58mm
it should have a nice "unique" uv spot pattern that highlights the card, not a repeated pattern, theres no originality there, and it will be disregarded.
The written material will be:
Corin Vale Hospitality College (logo)
Tobin Marsh
Director
Phone: 1300 615 737
Mobile: 0455 817 296
Email: info@corinvale.example
website: www.corinvale.example
I'm looking for originality here, i don't want just a simple stock card, want something that has a wow factor for people.
You will find the logo attached. you may invert the white to black words to suit the background as you please.
thank you and good luck
As a side note, ive received a lot of proposals, im too busy to give feedback to each and every one, so if i havent provided feedback for your design within 24 hours, then consider it not acceptable, and you could resubmit another design.
So far i have not seen any design that stood out for me, they all seem pretty generic. there nothing thats unique, i would figure for the amount that im offering, that people would put some more effort and creativity into the design.
so far over 200 designs submitted, and nothing i have seen looks very original, everything looks like a different variation of the same stuff, i said it very clearly i wanted something unique, the only thing that has come close to it so far is this one
Reason: Ive received alot of design concepts and i have reviewed everyone, but i havent had time to give feedback to every single one, only the ones that have interested me, if i havent responded, its because i havent found it good enough.
so far only a few design have been on par with what ive been looking for, an attractive eye popping design.
heres a few of them,
http://files.pixelbazaar.example/design_img/51736/62418/62418_2840915_51736_image.jpg
http://files.pixelbazaar.example/design_img/51736/68254/68254_2841377_51736_image.jpg
theyre, both unique and original, and eye catching, the only thing theyre missing is the sexyness.
if you still think you have some creativity left in your minds, then throw it on here.
Reason: Sorry guys for the delay, I was in a serious accident and out of commission for the past few months, I'm just slowly recovering now, please bare with me as i try to attend to this project, it may take me awhile as I have other projects that are on standby, I'm not 100% at the moment, so im extending the deadline for 2 weeks right now. Thanks for your patience.
Hospitality

```html
<!DOCTYPE html>
<html lang="en">
<head>
<meta charset="utf-8">
<title>Corin Vale Hospitality College – Business Card</title>
<link rel="stylesheet" href="https://fonts.googleapis.com/css2?family=Barlow+Condensed:wght@500;600&family=Barlow+Semi+Condensed:wght@500&display=swap">
<style>
  :root {
    --backdrop: #e4e4e4;
    --card-dark: #141518;
    --card-mid: #25272b;
    --accent-blue: #5aa8e0;
    --band-deep: #2f6fb4;
    --band-light: #76b8ea;
    --ink-white: #f4f4f4;
    --ink-grey: #8d8f93;
    --spot-tone: #34373d;
    --gloss: rgba(255,255,255,0.10);
  }
  * { margin: 0; padding: 0; box-sizing: border-box; }
  html, body {
    width: 1200px;
    height: 800px;
    overflow: hidden;
    background: var(--backdrop);
  }
  .sheet {
    width: 1200px;
    height: 800px;
    display: flex;
    align-items: center;
    justify-content: center;
    gap: 40px;
  }
  .card {
    position: relative;
    width: 520px;
    height: 336px;
    border-radius: 4px;
    overflow: hidden;
    background: linear-gradient(160deg, var(--card-mid) 0%, var(--card-dark) 70%);
    box-shadow: 0 12px 28px rgba(0,0,0,0.28);
  }

  /* Spot-UV varnish: gloss sheen across the card */
  .card__gloss {
    position: absolute;
    inset: 0;
    pointer-events: none;
    background:
      linear-gradient(112deg, transparent 38%, var(--gloss) 46%, rgba(255,255,255,0.03) 53%, transparent 60%),
      linear-gradient(112deg, transparent 64%, rgba(255,255,255,0.05) 68%, transparent 72%);
  }

  /* Front side */
  .card-front__pattern {
    position: absolute;
    inset: 0;
    background:
      radial-gradient(circle at 14% 28%, var(--spot-tone) 0%, transparent 22%),
      radial-gradient(circle at 86% 22%, var(--spot-tone) 0%, transparent 20%),
      radial-gradient(circle at 20% 82%, var(--spot-tone) 0%, transparent 22%),
      radial-gradient(circle at 82% 78%, var(--spot-tone) 0%, transparent 24%),
      radial-gradient(ellipse at 50% 50%, #202226 0%, var(--card-dark) 80%);
  }
  .card-front__mark {
    position: absolute;
    inset: 0;
    display: flex;
    align-items: center;
    justify-content: center;
    gap: 18px;
  }
  .brand-square {
    width: 40px;
    height: 40px;
    background: var(--accent-blue);
    flex: none;
  }
  .brand-name {
    font-family: "Barlow Condensed", sans-serif;
    font-weight: 600;
    color: var(--ink-white);
    text-transform: uppercase;
    letter-spacing: 0.02em;
    line-height: 0.98;
  }
  .card-front .brand-name { font-size: 38px; }

  /* Back side */
  .card-back__brand {
    position: absolute;
    left: 28px;
    top: 118px;
    display: flex;
    align-items: center;
    gap: 12px;
  }
  .card-back .brand-square { width: 26px; height: 26px; }
  .card-back .brand-name { font-size: 25px; width: 190px; }

  .contact {
    position: absolute;
    left: 276px;
    top: 100px;
    font-family: "Barlow Semi Condensed", sans-serif;
    font-weight: 500;
    color: var(--ink-white);
  }
  .contact__name {
    font-family: "Barlow Condensed", sans-serif;
    font-weight: 600;
    font-size: 25px;
    letter-spacing: 0.08em;
    color: var(--accent-blue);
    text-transform: uppercase;
    line-height: 1.1;
  }
  .contact__role {
    font-size: 14px;
    margin: 2px 0 8px;
  }
  .contact__list { list-style: none; }
  .contact__item {
    display: flex;
    align-items: center;
    gap: 10px;
    font-size: 16px;
    letter-spacing: 0.04em;
    line-height: 23px;
    white-space: nowrap;
  }
  .contact__icon { width: 14px; height: 14px; flex: none; }

  .card-back__band {
    position: absolute;
    left: 0;
    bottom: 0;
    width: 520px;
    height: 70px;
  }
  .card-back__web {
    position: absolute;
    left: 26px;
    bottom: 8px;
    font-family: "Barlow Semi Condensed", sans-serif;
    font-weight: 500;
    font-size: 15px;
    letter-spacing: 0.04em;
    color: var(--ink-white);
  }
</style>
</head>
<body>
<main class="sheet">

  <section class="card card-front" aria-label="Card front">
    <div class="card-front__pattern" role="img" aria-label="Spot-UV gloss pattern of scattered cocktail glasses, cherries, citrus slices and drink umbrellas"></div>
    <div class="card__gloss"></div>
    <div class="card-front__mark">
      <span class="brand-square"></span>
      <span class="brand-name">Corin Vale<br>Hospitality College</span>
    </div>
  </section>

  <section class="card card-back" aria-label="Card back">
    <div class="card__gloss"></div>
    <div class="card-back__brand">
      <span class="brand-square"></span>
      <span class="brand-name">Corin Vale Hospitality College</span>
    </div>

    <div class="contact">
      <p class="contact__name">Tobin Marsh</p>
      <p class="contact__role">Director</p>
      <ul class="contact__list">
        <li class="contact__item">
          <svg class="contact__icon" viewBox="0 0 16 16" aria-hidden="true"><path fill="#5aa8e0" d="M1 5.5C1 3 4 2 8 2s7 1 7 3.5l-3 1-1-2H5L4 6.5zM4 8h8l2 5H2z"/></svg>
          1300 615 737
        </li>
        <li class="contact__item">
          <svg class="contact__icon" viewBox="0 0 16 16" aria-hidden="true"><rect x="4" y="1" width="8" height="14" rx="1.5" fill="#5aa8e0"/><rect x="5.5" y="3" width="5" height="6" fill="#16171a"/></svg>
          0455 817 296
        </li>
        <li class="contact__item">
          <svg class="contact__icon" viewBox="0 0 16 16" aria-hidden="true"><rect x="1" y="3.5" width="14" height="9.5" fill="#5aa8e0"/><path d="M1 3.5l7 5.5 7-5.5" fill="none" stroke="#16171a" stroke-width="1.4"/></svg>
          info@corinvale.example
        </li>
      </ul>
    </div>

    <svg class="card-back__band" viewBox="0 0 520 70" aria-hidden="true">
      <defs>
        <linearGradient id="bandGradient" x1="0" y1="0" x2="0" y2="1">
          <stop offset="0" stop-color="#7bbcec"/>
          <stop offset="1" stop-color="#2f6fb4"/>
        </linearGradient>
        <linearGradient id="rimGradient" x1="0" y1="0" x2="1" y2="0">
          <stop offset="0" stop-color="#6f7277"/>
          <stop offset="1" stop-color="#b9bbbf"/>
        </linearGradient>
      </defs>
      <path d="M296 14 C304 14 306 4 314 4 H520 V14 Z" fill="url(#rimGradient)" opacity="0.6"/>
      <path d="M0 40 H266 C284 40 286 18 306 18 H520 V70 H0 Z" fill="url(#bandGradient)"/>
    </svg>
    <p class="card-back__web">www.corinvale.example</p>
  </section>

</main>
</body>
</html>
```